Hollarin Painting

Need business card design

Target Market(s)

Paint

Industry/Entity Type

Painting

Requirements
Must have
• Brice Halvorsen | Superviser
| HollaRin Painting
| mobile: (360) 555-0148
| email: Brice@hollarininc.example
| site: www.hollarininc.example
| address: 718 Marbeck St NE Ste 300, Olympia, WA 98577

```html
<!DOCTYPE html>
<html lang="en">
<head>
<meta charset="utf-8">
<title>HollaRin Painting — Business Card</title>
<link rel="stylesheet" href="https://fonts.googleapis.com/css2?family=Open+Sans:wght@400;600;800&display=swap">
<style>
  :root {
    --brand-blue: #1a3d85;
    --brand-green: #5fbf1f;
    --ink-grey: #6b6b6b;
    --card-white: #ffffff;
    --backdrop: #e9e9ea;
    --text-font: "Open Sans", Arial, sans-serif;
  }
  * { box-sizing: border-box; margin: 0; padding: 0; }
  html, body { width: 1200px; height: 899px; overflow: hidden; }
  body {
    background: var(--backdrop);
    font-family: var(--text-font);
    position: relative;
  }
  .card {
    position: absolute;
    left: 290px;
    width: 620px;
    height: 354px;
    overflow: hidden;
    box-shadow: 0 6px 18px rgba(0,0,0,0.15);
  }
  .card--front { top: 60px; background: var(--brand-blue); }
  .card--back { top: 474px; background: var(--card-white); }

  .brand-name {
    font-family: var(--text-font);
    font-weight: 800;
    letter-spacing: 1px;
    text-transform: uppercase;
    text-align: center;
    line-height: 1.1;
  }
  .card--front .brand-name {
    position: absolute;
    inset: 0;
    display: flex;
    align-items: center;
    justify-content: center;
    color: var(--card-white);
    font-size: 50px;
  }

  .back-brand {
    position: absolute;
    left: 30px;
    top: 70px;
    width: 300px;
    height: 140px;
    display: flex;
    align-items: center;
    justify-content: center;
  }
  .back-brand .brand-name { color: var(--brand-blue); font-size: 30px; }

  .divider {
    position: absolute;
    left: 360px;
    top: 40px;
    width: 2px;
    height: 200px;
    background: var(--brand-green);
  }

  .contact {
    position: absolute;
    left: 390px;
    top: 62px;
  }
  .contact__name {
    color: var(--brand-blue);
    font-weight: 800;
    font-size: 24px;
    line-height: 1;
  }
  .contact__role {
    color: var(--ink-grey);
    font-size: 13px;
    margin-top: 2px;
  }
  .contact__list { list-style: none; margin-top: 22px; }
  .contact__item {
    display: flex;
    align-items: center;
    gap: 8px;
    color: var(--ink-grey);
    font-size: 13.5px;
    margin-bottom: 10px;
  }
  .contact__icon { width: 20px; height: 20px; flex: none; }

  .address-band {
    position: absolute;
    left: 0;
    bottom: 0;
    width: calc(100% - 110px);
    height: 56px;
    background: var(--brand-green);
    display: flex;
    align-items: center;
    justify-content: center;
    gap: 12px;
    color: var(--card-white);
    font-size: 13px;
    letter-spacing: 1.8px;
    white-space: nowrap;
  }
  .address-band__icon { width: 22px; height: 22px; flex: none; }

  .corner-block {
    position: absolute;
    right: 0;
    bottom: 0;
    width: 110px;
    height: 56px;
    background: var(--brand-blue);
  }
  .corner-block svg { width: 100%; height: 100%; display: block; }
</style>
</head>
<body>

  <section class="card card--front" aria-label="Card front">
    <div class="brand-name">HollaRin Painting</div>
  </section>

  <section class="card card--back" aria-label="Card back">
    <div class="back-brand">
      <div class="brand-name">HollaRin<br>Painting</div>
    </div>

    <div class="divider"></div>

    <div class="contact">
      <div class="contact__name">Brice Halvorsen</div>
      <div class="contact__role">Superviser</div>
      <ul class="contact__list">
        <li class="contact__item">
          <svg class="contact__icon" viewBox="0 0 20 20" aria-hidden="true">
            <circle cx="10" cy="10" r="9" fill="none" stroke="#6b6b6b" stroke-width="1.2"/>
            <path d="M7 5.5c-.8.3-1.3 1-1.2 2 .4 3 3.5 6.3 6.6 6.8 1 .1 1.7-.4 2-1.2l-2-1.3-1 .8c-1.3-.6-2.5-1.8-3.1-3.1l.8-1z" fill="#6b6b6b"/>
          </svg>
          (360) 555-0148
        </li>
        <li class="contact__item">
          <svg class="contact__icon" viewBox="0 0 20 20" aria-hidden="true">
            <circle cx="10" cy="10" r="9" fill="none" stroke="#6b6b6b" stroke-width="1.2"/>
            <rect x="5.5" y="7" width="9" height="6.2" fill="#6b6b6b"/>
            <path d="M5.5 7l4.5 3.5L14.5 7" fill="none" stroke="#fff" stroke-width="0.9"/>
          </svg>
          Brice@hollarininc.example
        </li>
        <li class="contact__item">
          <svg class="contact__icon" viewBox="0 0 20 20" aria-hidden="true">
            <circle cx="10" cy="10" r="9" fill="none" stroke="#6b6b6b" stroke-width="1.2"/>
            <circle cx="10" cy="10" r="5" fill="none" stroke="#6b6b6b" stroke-width="0.9"/>
            <ellipse cx="10" cy="10" rx="2.2" ry="5" fill="none" stroke="#6b6b6b" stroke-width="0.8"/>
            <path d="M5 10h10M6 7.5h8M6 12.5h8" stroke="#6b6b6b" stroke-width="0.7"/>
          </svg>
          www.hollarininc.example
        </li>
      </ul>
    </div>

    <div class="address-band">
      <svg class="address-band__icon" viewBox="0 0 22 22" aria-hidden="true">
        <circle cx="11" cy="11" r="10" fill="none" stroke="#fff" stroke-width="1.3"/>
        <path d="M11 5.5a3.5 3.5 0 0 0-3.5 3.5c0 2.6 3.5 6.5 3.5 6.5s3.5-3.9 3.5-6.5A3.5 3.5 0 0 0 11 5.5z" fill="#fff"/>
        <circle cx="11" cy="9" r="1.3" fill="#5fbf1f"/>
      </svg>
      <span>718 Marbeck St NE Ste 300, Olympia, WA 98577</span>
    </div>

    <div class="corner-block">
      <svg viewBox="0 0 110 56" aria-hidden="true">
        <path d="M10 16h38M10 28h38M10 40h38" stroke="#fff" stroke-width="3" stroke-linecap="round"/>
        <rect x="66" y="0" width="5" height="56" fill="#5fbf1f"/>
        <rect x="78" y="0" width="5" height="56" fill="#5fbf1f"/>
        <rect x="90" y="0" width="5" height="56" fill="#5fbf1f"/>
      </svg>
    </div>
  </section>

</body>
</html>
```